Young and modern Electrical company working in the commercial arena.

Wanting a business card design thats modern and will last. Maybe Minimalist? Happy to look at changing my logo

Target Market(s)

Builders, Project Managers

Industry/Entity Type

Electrical

Contact Information for Business Card

Name
Address
Phone number
Job title

Logo Text

our name or just the logo i'm open to ideas

Font styles to use
Sans Serif

Requirements
Nice to have
• would like to keep the purple in our current logo. it's kinda unique to our market
Should not have
• Don't want it to be to busy. simple is best i think

```html
<!DOCTYPE html>
<html lang="en">
<head>
<meta charset="utf-8">
<title>Hallam Electrical – Business Card</title>
<link rel="stylesheet" href="https://fonts.googleapis.com/css2?family=Montserrat:wght@400;600;700&family=Lato:wght@400&display=swap">
<style>
  :root {
    --backdrop: #3a3a37;
    --card: #1a191c;
    --card-edge: #232226;
    --white: #f4f4f6;
    --purple: #6a45c9;
    --purple-soft: #7d5cd6;
  }
  * { box-sizing: border-box; margin: 0; padding: 0; }
  html, body { width: 1200px; height: 824px; overflow: hidden; }
  body {
    background: var(--backdrop);
    font-family: "Montserrat", sans-serif;
    display: flex;
    align-items: center;
    justify-content: center;
    gap: 50px;
  }
  .card {
    width: 525px;
    height: 300px;
    background: var(--card);
    border: 1px solid var(--card-edge);
    border-radius: 4px;
    box-shadow: 0 10px 30px rgba(0,0,0,.45);
    position: relative;
    color: var(--white);
  }
  /* Front */
  .card--front {
    display: flex;
    flex-direction: column;
    align-items: center;
    justify-content: center;
  }
  .brand {
    display: flex;
    align-items: center;
    gap: 12px;
  }
  .brand__mark {
    width: 14px;
    height: 14px;
    background: var(--purple);
  }
  .brand__name {
    font-weight: 600;
    color: var(--white);
    letter-spacing: 2px;
    line-height: 1.15;
    text-transform: uppercase;
  }
  .card--front .brand__name { font-size: 30px; }
  .website {
    margin-top: 22px;
    font-family: "Lato", sans-serif;
    font-size: 14px;
    letter-spacing: 2px;
    color: var(--purple-soft);
  }
  /* Back */
  .card--back {
    display: flex;
    align-items: center;
  }
  .back__brand {
    width: 235px;
    display: flex;
    justify-content: center;
  }
  .card--back .brand__name { font-size: 20px; }
  .divider {
    width: 2px;
    height: 170px;
    background: var(--purple);
  }
  .contact {
    padding-left: 30px;
  }
  .contact__name {
    font-weight: 700;
    font-size: 21px;
    letter-spacing: 1px;
    text-transform: uppercase;
  }
  .contact__title {
    font-size: 12px;
    letter-spacing: 1px;
    color: var(--purple-soft);
    text-transform: uppercase;
    margin-bottom: 14px;
  }
  .contact__list { list-style: none; }
  .contact__item {
    display: flex;
    align-items: center;
    gap: 10px;
    font-family: "Lato", sans-serif;
    font-size: 14px;
    line-height: 24px;
  }
  .contact__icon { width: 12px; height: 12px; fill: var(--purple-soft); flex: none; }
</style>
</head>
<body>
  <section class="card card--front">
    <div class="brand">
      <span class="brand__mark"></span>
      <span class="brand__name">Hallam<br>Electrical</span>
    </div>
    <p class="website">yourwebsite.com</p>
  </section>

  <section class="card card--back">
    <div class="back__brand">
      <div class="brand">
        <span class="brand__mark"></span>
        <span class="brand__name">Hallam<br>Electrical</span>
      </div>
    </div>
    <div class="divider"></div>
    <div class="contact">
      <h1 class="contact__name">Your Name</h1>
      <p class="contact__title">Job Title</p>
      <ul class="contact__list">
        <li class="contact__item">
          <svg class="contact__icon" viewBox="0 0 24 24" aria-hidden="true"><path d="M6.6 10.8a15 15 0 0 0 6.6 6.6l2.2-2.2c.3-.3.7-.4 1-.2 1.1.4 2.3.6 3.6.6.6 0 1 .4 1 1V20c0 .6-.4 1-1 1A17 17 0 0 1 3 4c0-.6.4-1 1-1h3.5c.6 0 1 .4 1 1 0 1.3.2 2.5.6 3.6.1.3 0 .7-.2 1z"/></svg>
          000 000 0000
        </li>
        <li class="contact__item">
          <svg class="contact__icon" viewBox="0 0 24 24" aria-hidden="true"><path d="M2 5h20v14H2z M2 5l10 8 10-8" fill="none" stroke="currentColor"/><path d="M2 5h20L12 13z M2 7l10 8 10-8v12H2z"/></svg>
          youremail@xyz.com
        </li>
        <li class="contact__item">
          <svg class="contact__icon" viewBox="0 0 24 24" aria-hidden="true"><path d="M12 2a7 7 0 0 0-7 7c0 5 7 13 7 13s7-8 7-13a7 7 0 0 0-7-7zm0 9.5A2.5 2.5 0 1 1 12 6.5a2.5 2.5 0 0 1 0 5z"/></svg>
          0000, Your address, ST
        </li>
      </ul>
    </div>
  </section>
</body>
</html>
```